Corvell Social "is a company that is focused on managing social media platforms.

I need a website design for a social media management company. The owner is a social media influencer in the Denver, Co area. Would like IG and Tik Tok page intergraded into the site. Would like all post from social to go directly to new website. Also put a page link for blog: her is my blog https://www.plumtrove.com/about

Target Market(s)

Any business that needs social media managed or video made for their company.

Coding

Coded - Design and coding required

Requirements
Must have
• Color scheme needs to match logo ; • IG: https://www.instagram.example/plum.trove/ • Clipwave: https://www.tiktok.example/@plum.trove Please add these videos: https://files.example/b-xQ7mLp2Rta
Nice to have
• • https://greyfinstudio.example/ "this a website that i like in the industry"

```html
<!DOCTYPE html>
<html lang="en">
<head>
<meta charset="utf-8">
<title>Corvell Social — Social Media Management in Denver</title>
<link rel="stylesheet" href="https://fonts.googleapis.com/css2?family=Montserrat:ital,wght@0,500;0,600;0,700;0,800;1,400&family=Poppins:ital,wght@0,400;0,500;0,600;0,700;1,400&display=swap">
<style>
:root{
  --navy:#0b1b3f;
  --navy-deep:#06102b;
  --navy-mid:#12295a;
  --cream:#f6ecd2;
  --mist:#e1e9f1;
  --ink:#17254a;
  --white:#ffffff;
  --rule:#1c2f5c;
}
*{box-sizing:border-box;margin:0;padding:0}
html,body{width:1200px;height:5222px;overflow:hidden}
body{position:relative;background:var(--white);color:var(--ink);font-family:"Poppins",sans-serif}
.abs{position:absolute}
a{color:inherit;text-decoration:none}

/* HERO */
.hero{position:absolute;left:0;top:0;width:1200px;height:780px;
  background:radial-gradient(ellipse at 20% 60%,#173a7a 0%,#0c2154 35%,var(--navy-deep) 75%);overflow:hidden}
.hero-wave{position:absolute;left:0;bottom:0;width:1200px;height:110px}
.follow{left:139px;top:56px;display:flex;align-items:center;gap:10px;font:500 13px "Montserrat",sans-serif;letter-spacing:1.5px;color:var(--white)}
.social-dot{display:inline-block;width:14px;height:14px;border-radius:50%;border:2px solid currentColor}
.brand-mark{width:72px;height:72px;border:2px solid var(--cream)}
.btn-outline{display:flex;align-items:center;justify-content:center;border:2px solid var(--cream);
  font:600 14px "Poppins",sans-serif;letter-spacing:1.5px;color:var(--cream);text-transform:uppercase}
.nav{top:120px;font:500 14px "Poppins",sans-serif;letter-spacing:1.5px;color:var(--white)}
.nav-brand{top:117px;left:487px;width:226px;text-align:center;font:500 15px "Poppins",sans-serif;letter-spacing:6px;color:var(--white);white-space:nowrap}
.hero-kicker{top:242px;width:1200px;text-align:center;font:600 28px "Montserrat",sans-serif;letter-spacing:3px;color:var(--white)}
.hero-title{top:292px;width:1200px;text-align:center;font:800 106px/0.92 "Montserrat",sans-serif;letter-spacing:3px;color:var(--cream)}

/* ABOUT */
.h-section{font:800 40px/1.05 "Montserrat",sans-serif;color:var(--navy);text-transform:uppercase}
.copy{font:400 15.5px/23px "Poppins",sans-serif;color:var(--ink)}
.photo{background:linear-gradient(135deg,#c9c9cf,#8a7e80 55%,#3d3336)}
.about-photo{left:602px;top:908px;width:414px;height:420px;border:4px solid var(--navy)}
.about-badge{left:888px;top:1204px;width:182px;height:182px;background:var(--navy);outline:3px solid var(--navy);border:6px solid var(--white);
  display:flex;align-items:center;justify-content:center;flex-direction:column;gap:10px;color:var(--cream);
  font:600 17px "Montserrat",sans-serif;letter-spacing:2px;text-align:center}
.about-badge i{display:block;width:22px;height:22px;border:2px solid var(--cream)}

/* GALLERY */
.gallery-title{top:1436px;width:1200px;text-align:center;font:800 38px "Montserrat",sans-serif;color:var(--navy)}
.gallery-sub{top:1484px;width:1200px;text-align:center;font:700 24px "Montserrat",sans-serif;color:var(--navy)}
.tile{width:233px}
.btn-solid{display:flex;align-items:center;justify-content:center;background:var(--navy);color:var(--white);
  font:600 15px "Poppins",sans-serif;letter-spacing:1.5px;text-transform:uppercase}

/* WHAT WE DO */
.services{left:0;top:2047px;width:1200px;height:742px;background:var(--mist)}
.accordion-row{left:116px;width:452px;height:56px;display:flex;align-items:center;justify-content:space-between;
  padding:0 12px;border-bottom:2px solid var(--navy);font:600 18px "Poppins",sans-serif;color:var(--navy)}
.accordion-row.is-open{background:#f4f7fa}
.accordion-row b{font-weight:500;font-size:18px}
.service-title{font:700 23px/29px "Montserrat",sans-serif;color:var(--navy)}
.service-sub{font:700 18px "Montserrat",sans-serif;color:var(--navy)}

/* WHY */
.why{left:0;top:2789px;width:1200px;height:608px;
  background:radial-gradient(ellipse at 50% 10%,#1a3570 0%,#0e224f 45%,var(--navy) 100%)}
.why-title{top:2876px;width:1200px;text-align:center;font:800 40px "Montserrat",sans-serif;color:var(--cream)}
.why-sub{top:2936px;left:270px;width:660px;text-align:center;font:400 15.5px/23px "Poppins",sans-serif;color:var(--white)}
.why-card{top:3034px;width:180px;height:213px;border:2px solid var(--cream);display:flex;flex-direction:column;align-items:center;
  padding-top:38px;text-align:center;font:700 14px/18px "Poppins",sans-serif;color:var(--white)}
.why-card svg{margin-bottom:20px}

/* STORIES */
.phone{border-radius:34px;background:#1a1a1e;padding:9px}
.phone-screen{width:100%;height:100%;border-radius:26px}
.btn-line{display:flex;align-items:center;justify-content:center;border:3px solid var(--navy);color:var(--navy);
  font:700 16px "Poppins",sans-serif;letter-spacing:.5px}

/* TESTIMONIALS */
.testimonials{left:0;top:4060px;width:1200px;height:440px;background:linear-gradient(180deg,#fff 0%,#f3f4f6 60%,#e9ebef 100%)}
.quote{top:4250px;left:272px;width:656px;text-align:center;font:italic 400 16px/27px "Poppins",sans-serif;color:var(--ink)}

/* CTA */
.cta{left:0;top:4500px;width:1200px;height:415px;
  background:radial-gradient(ellipse at 50% 100%,#1c4a9a 0%,#0f2a62 40%,var(--navy) 80%)}
.cta-title{top:4614px;width:1200px;text-align:center;font:800 39px/44px "Montserrat",sans-serif;color:var(--cream)}

/* FOOTER */
.footer{left:0;top:4936px;width:1200px;height:286px;background:var(--navy-deep)}
.footer-nav{top:5072px;font:500 14px "Poppins",sans-serif;letter-spacing:.5px;color:var(--white)}
</style>
</head>
<body>

<!-- HERO -->
<header class="hero" aria-label="Hero">
  <div class="abs" role="img" aria-label="Faint network of connected hexagons glowing in blue" style="left:0;top:300px;width:520px;height:420px;background:radial-gradient(circle at 30% 50%,rgba(80,140,230,.28),rgba(80,140,230,0) 70%)"></div>
  <svg class="hero-wave" viewBox="0 0 1200 110" preserveAspectRatio="none" aria-hidden="true">
    <path d="M0 68 C260 30 520 10 760 34 C930 52 1060 52 1200 26 L1200 110 L0 110 Z" fill="#ffffff"/>
  </svg>
</header>

<div class="abs follow">FOLLOW US <i class="social-dot"></i><i class="social-dot"></i><i class="social-dot"></i></div>
<div class="abs brand-mark" style="left:561px;top:30px" aria-hidden="true"></div>
<a class="abs btn-outline" href="#contact" style="left:803px;top:40px;width:254px;height:43px;font-size:13px">Get a free consultation</a>

<nav>
  <a class="abs nav" href="#" style="left:139px">HOME</a>
  <a class="abs nav" href="#about" style="left:238px">ABOUT</a>
  <a class="abs nav" href="#services" style="left:350px">SERVICES</a>
  <div class="abs nav-brand">CORVELL SOCIAL</div>
  <a class="abs nav" href="https://www.plumtrove.com/about" style="left:751px">BLOG</a>
  <a class="abs nav" href="#contact" style="left:847px">CONTACT</a>
  <a class="abs nav" href="#contact" style="left:980px">CONNECT</a>
</nav>

<p class="abs hero-kicker">DOES YOUR SOCIAL</p>
<h1 class="abs hero-title">INFLUENCE<br>CULTURE?</h1>
<a class="abs btn-outline" href="#contact" style="left:448px;top:520px;width:304px;height:51px;font-size:15px">Get a free consultation</a>

<!-- ABOUT -->
<section id="about">
  <h2 class="abs h-section" style="left:128px;top:870px">About us</h2>
  <div class="abs copy" style="left:128px;top:935px;width:440px">
    <p>Imagine your company's Snapline and Clipwave alive with engagement, capturing new audiences, and consistently driving measurable results. This is the elevated standard at Corvell Social, your dedicated social media management partner.</p>
    <p style="margin-top:23px">Founded by an influencer and content creator, Corvell Social brings an insider's understanding to crafting strategic narratives, creating visually stunning content, and leveraging the latest trends to catapult your online presence. Consider us your dedicated growth team right here in Denver, freeing you to concentrate on what you do best.</p>
    <p style="margin-top:23px">Ready to elevate your brand's impact through truly strategic social media?</p>
  </div>
  <div class="abs photo about-photo" role="img" aria-label="Portrait photo of the founder in a bright room"></div>
  <div class="abs about-badge"><i></i>CORVELL<br>SOCIAL</div>
</section>

<!-- GALLERY -->
<section aria-label="Latest posts">
  <h2 class="abs gallery-title">CORVELL SOCIAL:</h2>
  <p class="abs gallery-sub">Elevating Social That Drives Results.</p>
  <div class="abs photo tile" role="img" aria-label="Magazine cover feature of the founder" style="left:36px;top:1572px;height:248px;background:linear-gradient(135deg,#d8d8d8,#6f6a6a 50%,#2b2626)"></div>
  <div class="abs photo tile" role="img" aria-label="Two drink cans held outdoors" style="left:306px;top:1572px;height:248px;background:linear-gradient(135deg,#8a8e7a,#c7ccd6 50%,#4c4f40)"></div>
  <div class="abs photo tile" role="img" aria-label="Portrait of the founder at an event" style="left:576px;top:1596px;height:248px;background:linear-gradient(160deg,#3a3436,#8d8a92 55%,#d9d6dc)"></div>
  <div class="abs photo tile" role="img" aria-label="Row of colourful cocktails and plated food" style="left:843px;top:1565px;height:248px;background:linear-gradient(180deg,#3b2a22,#d99a3e 45%,#b74a3a 65%,#3a2418)"></div>
  <div class="abs photo tile" role="img" aria-label="Plated dessert on a dark table" style="left:1113px;top:1565px;height:248px;background:linear-gradient(135deg,#e9e3da,#5b4a3c 60%,#2a2018)"></div>
  <a class="abs btn-solid" href="#contact" style="left:448px;top:1887px;width:304px;height:51px">Get a free consultation</a>
</section>

<!-- WHAT WE DO -->
<section id="services">
  <div class="abs services"></div>
  <h2 class="abs h-section" style="left:128px;top:2205px">What we do</h2>
  <p class="abs copy" style="left:128px;top:2268px;width:465px">At Corvell Social, we craft bespoke social media strategies and execute meticulously, ensuring your brand not only stands out but also achieves its ambitious growth objectives. Our comprehensive suite of services is designed to <strong>elevate your brand perception while significantly increasing visibility.</strong></p>

  <div class="abs accordion-row is-open" style="top:2439px">Strategic Social Media Management<b>+</b></div>
  <div class="abs accordion-row" style="top:2500px">Premium Content Creation<b>+</b></div>
  <div class="abs accordion-row" style="top:2561px">Audience Engagement &amp; Growth<b>+</b></div>
  <div class="abs accordion-row" style="top:2622px">Targeted Reach &amp; Conversion<b>+</b></div>

  <svg class="abs" style="left:693px;top:2153px" width="100" height="104" viewBox="0 0 100 104" fill="none" stroke="#0b1b3f" stroke-width="3" aria-hidden="true">
    <rect x="42" y="4" width="54" height="42" rx="8"/>
    <path d="M58 36 V22 h6 l6 -10 c4 0 5 3 4 6 l-2 6 h10 c3 0 4 3 3 5 l-4 9 H58"/>
    <rect x="4" y="34" width="46" height="40" rx="8"/>
    <path d="M18 46 l-3 18 M30 46 l-3 18 M12 51 h24 M10 59 h24"/>
    <path d="M22 74 l6 8 l6 -8"/>
    <circle cx="52" cy="84" r="14"/>
    <path d="M45 82 c0 -6 7 -6 7 -1 c0 -5 7 -5 7 1 c0 4 -7 9 -7 9 c0 0 -7 -5 -7 -9 z"/>
  </svg>
  <h3 class="abs service-title" style="left:693px;top:2272px;width:360px">Strategic Social Media Management.</h3>
  <p class="abs copy" style="left:693px;top:2345px;width:375px">We provide end-to-end management of your social presence, ensuring every post aligns with your overarching brand goals and resonates deeply with your target audience. From engagement to campaign execution, we meticulously handle every detail.</p>
  <h4 class="abs service-sub" style="left:726px;top:2513px">Snapline &amp; Clipwave Management:</h4>
  <p class="abs copy" style="left:726px;top:2540px;width:345px">We cultivate compelling profiles and curate dynamic content tailored to each platform's unique algorithm and audience, fostering authentic connections and driving organic reach.</p>
</section>

<!-- WHY CHOOSE -->
<section aria-label="Why choose us">
  <div class="abs why"></div>
  <h2 class="abs why-title">WHY CHOOSE CORVELL SOCIAL?</h2>
  <p class="abs why-sub">Choosing the right social media partner is crucial for your brand's success. Here's why Corvell Social stands apart as your premier choice in Denver:</p>

  <div class="abs why-card" style="left:115px">
    <svg width="60" height="60" viewBox="0 0 60 60" fill="none" stroke="#fff" stroke-width="3.5"><path d="M52 24 A24 24 0 1 1 42 10"/><path d="M18 30 l10 10 l24 -26"/></svg>
    Insider<br>Expertise from<br>an Established<br>Influencer</div>
  <div class="abs why-card" style="left:313px">
    <svg width="60" height="60" viewBox="0 0 60 60" fill="none" stroke="#fff" stroke-width="3.5"><path d="M52 24 A24 24 0 1 1 42 10"/><path d="M18 30 l10 10 l24 -26"/></svg>
    Dedicated Local<br>Partnership</div>
  <div class="abs why-card" style="left:508px">
    <svg width="60" height="60" viewBox="0 0 60 60" fill="none" stroke="#fff" stroke-width="3.5"><path d="M52 24 A24 24 0 1 1 42 10"/><path d="M18 30 l10 10 l24 -26"/></svg>
    Unrivaled<br>Platform Mastery</div>
  <div class="abs why-card" style="left:707px">
    <svg width="60" height="60" viewBox="0 0 60 60" fill="none" stroke="#fff" stroke-width="3.5"><path d="M52 24 A24 24 0 1 1 42 10"/><path d="M18 30 l10 10 l24 -26"/></svg>
    Bespoke<br>Personalized<br>Service</div>
  <div class="abs why-card" style="left:904px">
    <svg width="60" height="60" viewBox="0 0 60 60" fill="none" stroke="#fff" stroke-width="3.5"><path d="M52 24 A24 24 0 1 1 42 10"/><path d="M18 30 l10 10 l24 -26"/></svg>
    Strategic,<br>Results-Driven<br>Approach</div>
</section>

<!-- CLIENT SUCCESS -->
<section aria-label="Client success stories">
  <h2 class="abs h-section" style="left:128px;top:3526px">Client<br>success stories</h2>
  <p class="abs copy" style="left:128px;top:3640px;width:462px">Sed ut perspiciatis unde omnis iste natus error sit volup tatem accusantium doloremque laudantium, totam rem aperiam, eaque ipsa quae ab illo inventore veritatis et quasi architecto beatae vitae dicta sunt explicabo. Nemo enim ipsam voluptatem quia voluptas sit aspernatur aut odit aut fugit, sed quia consequuntur magni dolores eos qui ratione voluptatem sequi nesciunt. Neque porro quisquam est, qui dolorem ipsum quia dolor sit amet, consectetur, adipisci velit.</p>
  <a class="abs btn-line" href="#" style="left:128px;top:3877px;width:142px;height:54px">VIEW MORE</a>

  <div class="abs" style="left:626px;top:3506px;width:450px;height:450px;border-radius:50%;background:#fdf5da"></div>
  <div class="abs phone" style="left:657px;top:3551px;width:200px;height:408px">
    <div class="phone-screen" role="img" aria-label="Client post: restaurant storefront at dusk" style="background:linear-gradient(180deg,#3b5a8a 0%,#2a3e63 40%,#b0382a 70%,#3a2a1c 100%)"></div>
  </div>
  <div class="abs phone" style="left:872px;top:3592px;width:182px;height:367px">
    <div class="phone-screen" style="background:linear-gradient(180deg,#ffffff 0%,#ffffff 45%,#f2d9a8 60%,#b5652e 80%,#f3efe6 100%)" role="img" aria-label="Client post: agency mark above a burger photo"></div>
  </div>
  <div class="abs" style="left:918px;top:3660px;width:86px;height:86px;background:var(--navy);border:3px solid var(--cream);display:flex;align-items:center;justify-content:center;font:600 11px/14px 'Montserrat',sans-serif;letter-spacing:1px;color:var(--cream);text-align:center">CORVELL<br>SOCIAL</div>
</section>

<!-- TESTIMONIALS -->
<section aria-label="Testimonials">
  <div class="abs testimonials"></div>
  <h2 class="abs" style="top:4100px;width:1200px;text-align:center;font:800 40px 'Montserrat',sans-serif;color:var(--navy)">TESTIMONIALS</h2>
  <svg class="abs" style="left:567px;top:4172px" width="66" height="50" viewBox="0 0 66 50" fill="none" stroke="#0b1b3f" stroke-width="2.5" aria-hidden="true">
    <path d="M28 6 C10 8 3 20 6 32 c2 8 14 10 18 3 c4 -7 -2 -14 -9 -12 c0 -7 6 -13 13 -14 z"/>
    <path d="M60 6 C42 8 35 20 38 32 c2 8 14 10 18 3 c4 -7 -2 -14 -9 -12 c0 -7 6 -13 13 -14 z"/>
  </svg>
  <p class="abs quote">Lorem ipsum dolor sit amet, consectetur adipiscing elit, sed do eiusmod tempor incididunt ut labore et dolore magna aliqua. Quis ipsum suspendisse ultrices gravida. Risus commodo viverra maecenas accumsan labore et dolore magna aliquaus ipsum suspendisse ultrices gravidisus commodo viverra maecenas accumsan lacus vel faices gravidisus commodo viverra maececilisis.</p>
  <p class="abs" style="top:4407px;width:1200px;text-align:center;font:700 16px 'Montserrat',sans-serif;color:var(--navy)">MARLA QUINN, CITY NAME</p>
</section>

<!-- CTA -->
<section id="contact" aria-label="Contact">
  <div class="abs cta"></div>
  <div class="abs" role="img" aria-label="Glowing hexagon network along the bottom edge" style="left:0;top:4760px;width:1200px;height:155px;background:linear-gradient(180deg,rgba(60,140,230,0),rgba(60,140,230,.35))"></div>
  <h2 class="abs cta-title">READY TO GROW YOUR SOCIAL?<br>CONTACT US TODAY!</h2>
  <a class="abs btn-outline" href="#contact" style="left:474px;top:4739px;width:250px;height:55px;border-color:var(--white);color:var(--white);font-weight:700;letter-spacing:.5px">CONTACT US TODAY</a>
</section>

<!-- FOOTER -->
<footer>
  <div class="abs footer"></div>
  <div class="abs" style="left:188px;top:5031px;width:76px;height:76px;border:2px solid var(--white)" aria-hidden="true"></div>
  <div class="abs" style="left:118px;top:5120px;width:220px;text-align:center;font:500 16px 'Poppins',sans-serif;letter-spacing:6px;color:var(--white);white-space:nowrap">CORVELL SOCIAL</div>
  <div class="abs" style="left:980px;top:5020px;display:flex;gap:10px;color:var(--white)"><i class="social-dot"></i><i class="social-dot"></i><i class="social-dot"></i></div>
  <a class="abs footer-nav" href="#" style="left:511px">HOME</a>
  <a class="abs footer-nav" href="#about" style="left:594px">ABOUT</a>
  <a class="abs footer-nav" href="#services" style="left:688px">SERVICES</a>
  <a class="abs footer-nav" href="https://www.plumtrove.com/about" style="left:808px">BLOG</a>
  <a class="abs footer-nav" href="#contact" style="left:888px">CONTACT</a>
  <a class="abs footer-nav" href="#contact" style="left:1000px">CONNECT</a>
  <p class="abs" style="left:664px;top:5116px;font:500 12.5px 'Poppins',sans-serif;color:var(--white)">COPYRIGHT 2025 CORVELL SOCIAL. ALL RIGHTS ARE RESERVED.</p>
</footer>

</body>
</html>
```